Easy Business Card / Presentation Cover Design Project

We are looking for a business card design, covers for powerpoint presentations for investors, and possibly simple stationary for a Chicago real estate development firm. Our new logo is attached below.

We rehab and provide newly constructed homes. We are not a real estate brokerage firm (i.e., agents such as Meridale 47) and only operate in the Chicago area.

In terms of design, sophisticated and high end that would appeal to investors (theme should resemble investment banks, hedge funds, private equity rather than tech startup).

Target Market(s)

Investors, banks, financing sources

Industry/Entity Type

Real Estate

Requirements
Must have
• Two deliverables here. 1) Business card 2) Covers for powerpoint presentation.

Must be able to look sophisticated and high end when printed. Please think through the type of printing that will be needed. Would prefer something that can be printed in raised ink but digital is ok as well.

Will be printed on heavy paper.

Business Card: Horizontal Layout, no black backgrounds,

For presentation front cover, should include logo only. For back cover, should include contact info. Horizontal and should not contain any information that will need to be changed (i.e. date or client name)
Nice to have
• Would like to have the edges colored but not required. Please show multiple designs
Should not have
• Should not have any die cut or embossed type of designs. Shape should be standard size.

We are not a design firm, a retail firm, or a consumer product firm.

Please do not incorporate a house, buildings, etc. This must be very professional looking.

```html
<!DOCTYPE html>
<html lang="en">
<head>
<meta charset="utf-8">
<title>Ardent Vale – Presentation Cover</title>
<link rel="stylesheet" href="https://fonts.googleapis.com/css2?family=Open+Sans:wght@400;600;700&display=swap">
<style>
  :root {
    --royal-blue: #135bc9;
    --accent-blue: #1e90ff;
    --sky-tint: #a9d6ff;
    --ice: #eef6fd;
    --ice-deep: #dcebfa;
    --white: #ffffff;
    --slate: #5b6068;
  }
  * { margin: 0; padding: 0; box-sizing: border-box; }
  html, body {
    width: 1200px;
    height: 900px;
    overflow: hidden;
    background: var(--royal-blue);
  }
  .cover {
    position: relative;
    width: 1200px;
    height: 900px;
    background: var(--royal-blue);
    font-family: "Open Sans", Arial, sans-serif;
    color: var(--white);
    overflow: hidden;
  }
  .cover-shapes {
    position: absolute;
    inset: 0;
    width: 1200px;
    height: 900px;
  }
  .client-block {
    position: absolute;
    left: 62px;
    top: 322px;
  }
  .client-name {
    font-size: 50px;
    font-weight: 700;
    letter-spacing: 0.5px;
    line-height: 1;
    white-space: nowrap;
  }
  .client-name .highlight { color: var(--sky-tint); }
  .client-address,
  .client-contact {
    list-style: none;
    font-size: 22px;
    font-weight: 600;
    line-height: 37px;
  }
  .client-address { margin-top: 42px; margin-left: 3px; }
  .client-contact { margin-top: 16px; margin-left: 2px; }
  .client-contact li:nth-child(2) { margin-left: 3px; }
  .brand-name {
    position: absolute;
    left: 862px;
    top: 338px;
    display: flex;
    align-items: center;
    gap: 14px;
    font-family: "Open Sans", Arial, sans-serif;
    font-size: 42px;
    font-weight: 600;
    color: var(--slate);
    white-space: nowrap;
  }
  .brand-dot {
    width: 22px;
    height: 22px;
    border-radius: 50%;
    background: var(--accent-blue);
  }
</style>
</head>
<body>
  <main class="cover">
    <svg class="cover-shapes" viewBox="0 0 1200 900" aria-hidden="false">
      <defs>
        <radialGradient id="emblem-glow" cx="0.45" cy="0.5" r="0.6">
          <stop offset="0" stop-color="#f6fbff"/>
          <stop offset="0.7" stop-color="#e6f1fc"/>
          <stop offset="1" stop-color="#d7e8f8"/>
        </radialGradient>
        <linearGradient id="footer-wash" x1="0" y1="0" x2="1" y2="0">
          <stop offset="0" stop-color="#e3effb"/>
          <stop offset="1" stop-color="#f3f9ff"/>
        </linearGradient>
      </defs>

      <!-- emblem oval -->
      <ellipse class="emblem-ring" cx="1058" cy="369" rx="262" ry="201" fill="var(--accent-blue)"/>
      <ellipse class="emblem-field" cx="1072" cy="372" rx="262" ry="192"
               fill="url(#emblem-glow)" role="img"
               aria-label="Soft light-blue backdrop for the company name"/>

      <!-- footer band -->
      <path class="footer-line" d="M0 800 C 300 790, 650 830, 930 900 L 0 900 Z" fill="var(--accent-blue)"/>
      <path class="footer-band" d="M0 810 C 300 800, 640 840, 905 900 L 0 900 Z"
            fill="url(#footer-wash)" role="img"
            aria-label="Pale blue footer band"/>
    </svg>

    <section class="client-block">
      <h1 class="client-name"><span class="highlight">COMPANY</span> CLIENT NAME</h1>
      <ul class="client-address">
        <li>Company Address 1</li>
        <li>Company Address 2</li>
      </ul>
      <ul class="client-contact">
        <li>Phone : 00 00 0121</li>
        <li>Telefax : 00 00 0121</li>
      </ul>
    </section>

    <div class="brand-name">
      <span class="brand-dot"></span>
      <span>Ardent Vale</span>
    </div>
  </main>
</body>
</html>
```